Child-Biting, Chorizo and Chancing Your Arm

Looking to get a book cover designed.

I am an entrepreneur with an edge (I am fun, outgoing and with tons of personality) and run a localisation company called Tonglingo. My book is my story, some business lessons and also some language lessons and idioms. I am an entrepreneur who has set up his business in a country other than his, with a different language - and thus my book talks about communication and the problems that do arise when things get lost in translation.

I have included, attached, a document with three forewords/introductions from others about the book.

The title of the book is:

Child-Biting,
Chorizo
and Chancing Your Arm
(whatever that means) [in small letters]

And the subtitle:
How a lonely Spaniard made it big in Britain

Notes:

I was a child biter
I am from Spain - thus chorizo
And I set a business up in the UK - took a risk "chance my arm"

Also, may be a good idea (depends how it looks) to have "whatever that means" in small letters after chancing your arm, since most English people do not know the meaning of this expression. And I constantly play on words with communication throughout the book.

Style notes:

The book is fun, entertaining and I do not take myself too seriously, so I want the cover to be professional, bold and striking.

I like the colours black and red, but these are not a must. The idea is to make the cover stand out, while still remain professional.

--------
Chancing Your Arm: http://www.brennockabbey.example/chancing-your-arm.aspx

Target Market(s)

Entrepreneurs, business owners, linguists, people that work in large organisations but appreciate a bit of a human/personal touch.

Industry/Entity Type

Business

Font styles to use
Sans Serif
Other font styles liked:
• Modern font.

Colors
ec1f27
ffffff
000000
d5d5d5
0355a3

Requirements
Nice to have
• Bold statement
• Striking but classy
• Fun
• Different
• Stand out
Should not have
• Traditional boring style
• Yellow colour

```html
<!DOCTYPE html>
<html lang="en">
<head>
<meta charset="utf-8">
<title>Child-Biting, Chorizo and Chancing Your Arm – Book Cover</title>
<link href="https://fonts.googleapis.com/css2?family=Freckle+Face&family=Open+Sans:wght@400&family=Oswald:wght@500&display=swap" rel="stylesheet">
<style>
  :root {
    --bg: #2a2a2c;
    --back-black: #0c0c0c;
    --back-grain: #1b1b1b;
    --paper-light: #d9b996;
    --paper-mid: #c79a74;
    --paper-edge: #b0674a;
    --title-red: #d4121c;
    --title-outline: #e8b53a;
    --title-glow: #3fb6e8;
    --fold-line: rgba(120, 80, 55, 0.45);
    --sub-pink: #e8225c;
    --sub-blue: #1d6fb8;
    --author-blue: #0355a3;
    --chorizo: #b8202a;
    --white: #ffffff;
  }
  html, body {
    margin: 0;
    width: 1200px;
    height: 800px;
    overflow: hidden;
    background: var(--bg);
  }
  .canvas {
    position: relative;
    width: 1200px;
    height: 800px;
  }
  .back-cover {
    position: absolute;
    left: 90px;
    top: 40px;
    width: 480px;
    height: 720px;
    background: repeating-linear-gradient(90deg, var(--back-black) 0 2px, var(--back-grain) 2px 3px, var(--back-black) 3px 6px);
    display: flex;
    flex-direction: column;
    justify-content: center;
    align-items: center;
    box-sizing: border-box;
    padding: 0 56px 60px;
  }
  .back-copy {
    font-family: "Open Sans", sans-serif;
    font-size: 14.5px;
    line-height: 1.85;
    color: var(--white);
    text-align: center;
    margin: 0 0 18px;
  }
  .front-cover {
    position: absolute;
    left: 630px;
    top: 40px;
    width: 480px;
    height: 720px;
    background:
      radial-gradient(ellipse at 50% 45%, var(--paper-light) 0%, var(--paper-mid) 65%, var(--paper-edge) 100%);
    overflow: hidden;
  }
  .fold {
    position: absolute;
    left: 0;
    width: 100%;
    height: 2px;
    background: var(--fold-line);
  }
  .title {
    position: absolute;
    left: 0;
    width: 100%;
    margin: 0;
    text-align: center;
    font-family: "Freckle Face", cursive;
    font-weight: 400;
    color: var(--title-red);
    -webkit-text-stroke: 2px var(--title-outline);
    paint-order: stroke fill;
    text-shadow: -3px 2px 0 var(--title-glow);
    line-height: 1;
  }
  .title-line { position: absolute; left: 0; width: 100%; display: block; }
  .line-1 { top: 150px; font-size: 66px; }
  .line-2 { top: 250px; font-size: 72px; }
  .line-3 { top: 345px; font-size: 64px; }
  .line-4 { top: 445px; font-size: 66px; }
  .chorizo-o {
    display: inline-block;
    width: 44px;
    height: 48px;
    border-radius: 50%;
    background: radial-gradient(circle, #d64a4a, var(--chorizo));
    vertical-align: -2px;
    margin: 0 2px;
  }
  .aside {
    position: absolute;
    top: 535px;
    left: 0;
    width: 100%;
    text-align: center;
    font-family: "Freckle Face", cursive;
    font-size: 34px;
    color: var(--title-red);
    -webkit-text-stroke: 1.5px var(--title-outline);
    paint-order: stroke fill;
    transform: rotate(3deg);
    margin: 0;
  }
  .subtitle {
    position: absolute;
    top: 585px;
    left: 130px;
    margin: 0;
    font-family: "Open Sans", sans-serif;
    font-size: 17px;
    line-height: 1.6;
  }
  .subtitle .part-a { color: var(--sub-pink); display: block; }
  .subtitle .part-b { color: var(--sub-blue); display: block; padding-left: 90px; }
  .author {
    position: absolute;
    top: 640px;
    left: 0;
    width: 100%;
    text-align: center;
    font-family: "Oswald", sans-serif;
    font-weight: 500;
    font-size: 52px;
    color: var(--author-blue);
    margin: 0;
    letter-spacing: 0;
  }
</style>
</head>
<body>
<main class="canvas">
  <section class="back-cover" aria-label="Back cover">
    <p class="back-copy">Books may also refer to works of literature, or a main division of such a work. In library and information science, a book is called a monograph, to distinguish it from serial periodicals such as magazines, journals or newspapers. The body of all written works including books is literature. In novels and sometimes other types of books (for example, biographies), a book may be divided into several large sections, also called books (Book 1, Book 2, Book 3, and so on). An avid reader of books is a bibliophile or colloquially, bookworm.</p>
    <p class="back-copy">A shop where books are bought and sold is a bookshop or bookstore. Books can also be borrowed from libraries. Libraria has estimated that as of 2010, approximately 130,000,000 unique titles had been published</p>
  </section>

  <section class="front-cover" aria-label="Front cover">
    <div class="fold" style="top:238px"></div>
    <div class="fold" style="top:336px"></div>
    <div class="fold" style="top:432px"></div>
    <h1 class="title">
      <span class="title-line line-1">Child-Biting,</span>
      <span class="title-line line-2">Ch<span class="chorizo-o" role="img" aria-label="Slice of chorizo in place of the letter o"></span>rizo</span>
      <span class="title-line line-3">and Chancing</span>
      <span class="title-line line-4">Your Arm</span>
    </h1>
    <p class="aside">whatever that mean?</p>
    <p class="subtitle"><span class="part-a">How a lonely Spaniard</span><span class="part-b">made it big in Britain</span></p>
    <p class="author">AUTHOR NAME</p>
  </section>
</main>
</body>
</html>
```